Cool modern, tech Business card design

Looking for a new business card design for our Managed IT Services company. We would like 2 sides, with the logo one one side horizontally and then the information on the back in either vertical or horizontal. We want our colors from the logo incorporated but also would like to see the color gray in there as well.

Target Market(s)

IT, Information Technology, Tech, Service

Industry/Entity Type

It Service

Contact Information for Business Card

Carl Penner
Managing Partner
(P)555-271-4830 ext xxx
(F)555-271-4831
www.brixtelcore.com

Font styles to use
Sans Serif

Colors
959595
000000
ec1f27

Requirements
Must have
• Logo on one side with some nice design or pattern
• Information on back in either vertical or horizontal format
Nice to have
• For it to look cool, tech, modern, stand out.

```html
<!DOCTYPE html>
<html lang="en">
<head>
<meta charset="utf-8">
<title>Brixtelcore Business Card</title>
<link rel="stylesheet" href="https://fonts.googleapis.com/css2?family=Work+Sans:wght@400;500;600&display=swap">
<style>
  :root {
    --stage: #2a2a2b;
    --card: #1b1b1c;
    --card-edge: #262627;
    --brand-red: #ec1f27;
    --brand-gray: #959595;
    --ink-white: #f4f4f4;
    --ink-soft: #d9d9d9;
  }
  * { box-sizing: border-box; margin: 0; padding: 0; }
  html, body {
    width: 1200px; height: 900px; overflow: hidden;
    background: var(--stage);
    font-family: "Work Sans", sans-serif;
  }
  .canvas {
    position: relative; width: 1200px; height: 900px;
    display: flex; flex-direction: column; align-items: center; justify-content: center; gap: 40px;
  }
  .card {
    position: relative; width: 700px; height: 400px;
    background: linear-gradient(135deg, var(--card) 0%, var(--card-edge) 100%);
    box-shadow: 0 12px 30px rgba(0,0,0,0.45);
  }
  .card-front { display: flex; align-items: center; justify-content: center; }
  .wordmark {
    display: flex; align-items: center; gap: 14px;
    font-weight: 500; letter-spacing: -0.5px; line-height: 1;
  }
  .wordmark-square { width: 22px; height: 22px; border-radius: 4px; }
  .card-front .wordmark { font-size: 64px; color: var(--brand-gray); }
  .card-front .wordmark-square { background: var(--brand-gray); }

  .card-back { display: flex; align-items: center; }
  .back-brand {
    width: 360px; display: flex; justify-content: center;
  }
  .card-back .wordmark { font-size: 48px; color: var(--ink-white); }
  .card-back .wordmark-square { background: var(--brand-red); width: 18px; height: 18px; }
  .divider {
    width: 2px; height: 190px; background: var(--brand-red);
  }
  .contact { padding-left: 26px; color: var(--ink-white); }
  .contact-name {
    font-size: 28px; font-weight: 500; color: var(--brand-red);
    letter-spacing: 0.5px; line-height: 1;
  }
  .contact-title { font-size: 15px; margin-top: 4px; color: var(--ink-soft); letter-spacing: 0.4px; }
  .contact-address { font-size: 15px; margin-top: 14px; line-height: 1.35; letter-spacing: 0.3px; }
  .contact-list { list-style: none; margin-top: 12px; font-size: 15px; letter-spacing: 0.3px; }
  .contact-list li { display: flex; align-items: center; gap: 10px; line-height: 1.5; }
  .contact-list svg { width: 11px; height: 11px; flex: none; fill: none; stroke: var(--brand-red); stroke-width: 2; }
  .contact-list svg.solid { fill: var(--brand-red); stroke: none; }
</style>
</head>
<body>
<main class="canvas">
  <section class="card card-front" aria-label="Card front">
    <div class="wordmark"><span>brixtelcore</span><span class="wordmark-square"></span></div>
  </section>

  <section class="card card-back" aria-label="Card back">
    <div class="back-brand">
      <div class="wordmark"><span>brixtelcore</span><span class="wordmark-square"></span></div>
    </div>
    <div class="divider"></div>
    <div class="contact">
      <p class="contact-name">CARL PENNER</p>
      <p class="contact-title">Managing Partner</p>
      <p class="contact-address">42 Alder Lane<br>Westbury, New York 11590</p>
      <ul class="contact-list">
        <li>
          <svg class="solid" viewBox="0 0 12 12"><path d="M2 1h3l1 3-2 1a7 7 0 0 0 3 3l1-2 3 1v3c-6 0-9-3-9-9z"/></svg>
          555-271-4830 ext xxx
        </li>
        <li>
          <svg class="solid" viewBox="0 0 12 12"><rect x="3" y="1" width="6" height="3"/><rect x="1" y="5" width="10" height="4" rx="1"/><rect x="3" y="8" width="6" height="3"/></svg>
          555-271-4831
        </li>
        <li>
          <svg viewBox="0 0 12 12"><rect x="1" y="2.5" width="10" height="7"/><path d="M1 3l5 4 5-4"/></svg>
          info@brixtelcore.com
        </li>
        <li>
          <svg viewBox="0 0 12 12"><circle cx="6" cy="6" r="5"/><ellipse cx="6" cy="6" rx="2" ry="5"/><path d="M1 6h10"/></svg>
          www.brixtelcore.com
        </li>
      </ul>
    </div>
  </section>
</main>
</body>
</html>
```